I would like to design a flyer that I can put on car windows, inside peoples mailboxes. This flyer is to display Crestline Athletics and Wellness is now Open. I would like this to be a Free One Week Pass! I would like to have the following information on the flyer.
1) My logo - CRESTLINE ATHLETICS AND WELLNESS (I will upload the logo)
2) Hours of operation - Mon - Fri "5am - 10pm" Sat/Sun "6am -6pm"
3) Membership $59.00 "No Initiation Fee" Month to Month Membership.
Class are free. The Classes are Yoga, Salsa Classes, Bootcamps, HITT, Sports Performance,
4) Personal Training
5) Message Therapy
6) Address: 2871 Havelmoor Commerce Dr. Suite 213
Chantilly, VA 20347
7) mail@crestlineaw-example.com
8) Free One Week Pass

```html
<!DOCTYPE html>
<html lang="en">
<head>
<meta charset="utf-8">
<title>Crestline Athletics and Wellness – Now Opening</title>
<link rel="stylesheet" href="https://fonts.googleapis.com/css2?family=Kaushan+Script&family=Roboto:wght@400;500&display=swap">
<style>
  :root {
    --brand-red: #e8202a;
    --ink: #4a4a4c;
    --band: #4b4c4e;
    --paper: #ffffff;
    --white: #ffffff;
    --script-grey: #505052;
  }
  html, body {
    margin: 0;
    padding: 0;
    width: 1200px;
    height: 825px;
    overflow: hidden;
    background: var(--paper);
  }
  .flyer {
    position: relative;
    width: 1200px;
    height: 825px;
    overflow: hidden;
    background: var(--paper);
    font-family: "Roboto", Arial, sans-serif;
    color: var(--ink);
  }
  .flyer p { margin: 0; position: absolute; white-space: nowrap; line-height: 1.2; }

  /* hero illustration area: ribbon with exercising silhouettes */
  .hero-illustration {
    position: absolute;
    left: 440px; top: 192px;
    width: 730px; height: 400px;
    border-radius: 24px;
    background: linear-gradient(120deg, rgba(232,32,42,0.10) 0%, rgba(232,32,42,0.32) 55%, rgba(200,20,29,0.22) 100%);
  }

  .bottom-band { position: absolute; left: 0; top: 0; }

  /* brand */
  .brand-mark {
    position: absolute;
    left: 90px; top: 58px;
    width: 166px; height: 166px;
    border-radius: 50%;
    background: var(--brand-red);
  }
  .brand-name {
    position: absolute;
    left: 278px; top: 72px;
    margin: 0;
    font-weight: 500;
    color: var(--brand-red);
  }
  .brand-name span { display: block; white-space: nowrap; }
  .brand-name .brand-main { font-size: 84px; line-height: 96px; letter-spacing: 1px; }
  .brand-name .brand-sub { font-size: 24px; line-height: 30px; letter-spacing: 4.5px; margin-left: 3px; }

  /* opening headline */
  .now { left: 956px; top: 22px; font-size: 35px; color: var(--script-grey); }
  .opening {
    left: 868px; top: 52px;
    font-family: "Kaushan Script", cursive;
    font-size: 72px;
    color: var(--script-grey);
    transform: rotate(-4deg);
  }

  /* membership offer */
  .membership { left: 95px; top: 281px; font-size: 45px; font-weight: 500; }
  .membership .price { color: var(--brand-red); }
  .offer-line { left: 95px; font-size: 30px; }
  .offer-line.no-fee { top: 362px; }
  .offer-line.month { top: 401px; }
  .classes { left: 95px; top: 464px; font-size: 38px; color: var(--brand-red); }
  .join { left: 96px; top: 553px; font-size: 31px; }

  /* service tags */
  .service-tag {
    position: absolute;
    right: 0;
    height: 45px;
    color: var(--white);
    font-size: 24px;
    line-height: 45px;
    box-sizing: border-box;
    clip-path: polygon(24px 0, 100% 0, 100% 100%, 0 100%);
  }
  .service-tag.training {
    top: 382px; width: 308px; padding-left: 63px;
    background: var(--brand-red);
  }
  .service-tag.therapy {
    top: 439px; width: 345px; padding-left: 87px;
    background: var(--band);
  }

  /* pass & hours */
  .pass { left: 754px; top: 596px; font-size: 42px; color: var(--white); }
  .pass-rule {
    position: absolute;
    left: 755px; top: 656px;
    width: 403px; height: 2px;
    background: var(--white);
  }
  .hours-title { right: 46px; top: 682px; font-size: 28px; color: var(--white); }
  .hours-line { right: 44px; font-size: 28px; color: var(--white); }
  .hours-line.weekday { top: 728px; }
  .hours-line.weekend { top: 766px; }
  .hours-line .slash { color: var(--brand-red); }

  /* contact */
  .address { left: 88px; top: 721px; font-size: 21px; color: var(--white); }
  .email { left: 88px; top: 756px; font-size: 21px; color: var(--white); }
</style>
</head>
<body>
<main class="flyer">
  <div class="hero-illustration" role="img"
       aria-label="Red ribbon swirling upward with silhouettes of people doing sit-ups, yoga, dancing and leaping"></div>

  <svg class="bottom-band" width="1200" height="825" viewBox="0 0 1200 825" aria-hidden="true">
    <polygon points="0,706 1200,510 1200,825 0,825" fill="var(--band)"/>
  </svg>

  <div class="brand-mark" aria-hidden="true"></div>
  <h1 class="brand-name"><span class="brand-main">CRESTLINE</span><span class="brand-sub">ATHLETICS AND WELLNESS</span></h1>

  <p class="now">Now</p>
  <p class="opening">Opening</p>

  <p class="membership">Membership <span class="price">$59.00</span></p>
  <p class="offer-line no-fee">“No Initiation Fee”</p>
  <p class="offer-line month">Month to Month Membership</p>
  <p class="classes">Class are free</p>
  <p class="join">Come &amp; Join Us!</p>

  <div class="service-tag training">Personal Training</div>
  <div class="service-tag therapy">Message Therapy</div>

  <p class="pass">Free One Week Pass</p>
  <div class="pass-rule" aria-hidden="true"></div>
  <p class="hours-title">Hours of operation</p>
  <p class="hours-line weekday">Mon <span class="slash">/</span>Fri :&nbsp; 5am - 10pm</p>
  <p class="hours-line weekend">Sat <span class="slash">/</span>Sun :&nbsp; 6am -&nbsp; 6pm</p>

  <p class="address">2871 Havelmoor Commerce Dr. Suite 213 Chantilly, VA 20347</p>
  <p class="email">mail@crestlineaw-example.com</p>
</main>
</body>
</html>
```